Bold Biz Card & Stationary for a Marketing Company
Cobalt Heron Marketing Solutions
Bright & Fun-filled
Linda Hollow
Owner
2417 Maple Ridge Dr
Longmont CO 80503
lindahollow@cobaltheronmarketing.example
cobaltheronmarketing.example
I want something that is unique and/or eye catching.

```html
<!DOCTYPE html>
<html lang="en">
<head>
<meta charset="utf-8">
<title>Cobalt Heron Marketing Solutions — Stationery</title>
<link rel="stylesheet" href="https://fonts.googleapis.com/css2?family=Montserrat:wght@400;600;700;800&family=Open+Sans:wght@400;600&display=swap">
<style>
  :root {
    --bg: #232325;
    --paper: #ffffff;
    --ink: #1b1b1b;
    --band: #161616;
    --orange: #ee6a23;
    --red: #d8262b;
    --grey: #6d6d6d;
    --light: #e9e9e9;
    --dark-card: #2b2b2d;
  }
  * { box-sizing: border-box; margin: 0; padding: 0; }
  html, body { width: 1200px; height: 708px; overflow: hidden; }
  body {
    background: var(--bg);
    font-family: "Open Sans", Arial, sans-serif;
    color: var(--ink);
    position: relative;
  }
  .sheet { position: absolute; background: var(--paper); box-shadow: 0 6px 18px rgba(0,0,0,.45); overflow: hidden; }

  /* brand lockup */
  .brand { display: flex; align-items: center; gap: 10px; }
  .brand-dot { border-radius: 50%; background: var(--orange); flex: none; }
  .brand-name {
    font-family: "Montserrat", Arial, sans-serif; font-weight: 800;
    color: var(--orange); text-transform: uppercase; line-height: 1.1; letter-spacing: .04em;
    white-space: nowrap;
  }

  .header-band { position: absolute; left: 0; right: 0; top: 0; background: var(--band); border-bottom: 3px solid var(--orange); }

  /* letterhead */
  .letterhead { left: 70px; top: 108px; width: 380px; height: 492px; }
  .letterhead .header-band { height: 52px; }
  .letterhead .brand { position: absolute; left: 22px; top: 13px; }
  .letterhead .brand-dot { width: 26px; height: 26px; }
  .letterhead .brand-name { font-size: 11px; }
  .letter-body { position: absolute; left: 30px; right: 30px; top: 88px; font-size: 7.4px; line-height: 1.65; color: #444; }
  .letter-body .salutation { font-weight: 600; color: var(--ink); margin-bottom: 10px; }
  .letter-body p { margin-bottom: 9px; }
  .letter-body .signoff { margin-top: 16px; }
  .letter-body .signer { font-family: "Montserrat", Arial, sans-serif; font-weight: 700; color: var(--orange); font-size: 8.5px; margin-top: 14px; }
  .letter-footer {
    position: absolute; left: 30px; right: 30px; bottom: 18px; padding-top: 7px;
    border-top: 1px solid var(--light); font-size: 6.4px; color: var(--grey); display: flex; justify-content: space-between;
  }

  /* envelope */
  .envelope { left: 520px; top: 48px; width: 600px; height: 240px; }
  .envelope .header-band { right: auto; width: 300px; height: 46px; }
  .envelope .brand { position: absolute; left: 20px; top: 11px; }
  .envelope .brand-dot { width: 24px; height: 24px; }
  .envelope .brand-name { font-size: 10px; }
  .envelope .return-address { position: absolute; left: 22px; top: 60px; font-size: 7px; color: var(--grey); line-height: 1.5; }
  .envelope .window { position: absolute; left: 40px; top: 128px; width: 230px; height: 76px; border: 1px solid #cfcfcf; border-radius: 4px; background: #f1f2f3; }

  /* business cards */
  .card { width: 290px; height: 166px; border-radius: 6px; }
  .card .header-band { height: 38px; }
  .card .brand { position: absolute; left: 14px; top: 10px; }
  .card .brand-dot { width: 20px; height: 20px; }
  .card .brand-name { font-size: 8.5px; }

  .person { position: absolute; left: 16px; top: 58px; }
  .person-name { font-family: "Montserrat", Arial, sans-serif; font-weight: 700; color: var(--orange); font-size: 13px; }
  .person-role { font-size: 8px; color: var(--grey); text-transform: uppercase; letter-spacing: .12em; margin-top: 2px; }
  .contact-list { position: absolute; left: 16px; right: 12px; top: 98px; list-style: none; font-size: 7.2px; color: #444; }
  .contact-list li { display: flex; align-items: center; gap: 6px; margin-bottom: 4px; white-space: nowrap; }
  .contact-list svg { width: 8px; height: 8px; flex: none; fill: var(--orange); }

  .card-contact { left: 680px; top: 318px; }
  .card-web { left: 520px; top: 508px; }

  .card-dark { left: 830px; top: 508px; background: var(--dark-card); }
  .card-dark .brand { left: 50%; top: 50%; transform: translate(-50%, -50%); flex-direction: column; gap: 8px; text-align: center; }
  .card-dark .brand-dot { width: 30px; height: 30px; }
  .card-dark .brand-name { font-size: 11px; }
  .card-dark .accent { position: absolute; left: 0; right: 0; bottom: 0; height: 4px; background: var(--orange); }
</style>
</head>
<body>

  <!-- Letterhead -->
  <section class="sheet letterhead">
    <div class="header-band">
      <div class="brand"><span class="brand-dot"></span><span class="brand-name">Cobalt Heron Marketing Solutions</span></div>
    </div>
    <div class="letter-body">
      <div class="salutation">Dear Sir / Madame,</div>
      <p>Thank you for your interest in our services. We build bright campaigns that help small businesses grow, connect with new customers and stand out in busy local markets with clear messages and friendly design.</p>
      <p>Our team plans each project from the first idea to the final print, keeping every detail on time and on budget so you can focus on running your business.</p>
      <p>Please reach out at any time to schedule a free consultation. We look forward to working with you.</p>
      <div class="signoff">Sincerely,</div>
      <div class="signer">Linda Hollow</div>
    </div>
    <footer class="letter-footer">
      <span>2417 Maple Ridge Dr, Longmont CO 80503</span>
      <span>303.555.0147</span>
      <span>cobaltheronmarketing.example</span>
    </footer>
  </section>

  <!-- Envelope -->
  <section class="sheet envelope">
    <div class="header-band">
      <div class="brand"><span class="brand-dot"></span><span class="brand-name">Cobalt Heron Marketing Solutions</span></div>
    </div>
    <div class="return-address">2417 Maple Ridge Dr<br>Longmont CO 80503</div>
    <div class="window"></div>
  </section>

  <!-- Business card: contact -->
  <section class="sheet card card-contact">
    <div class="header-band">
      <div class="brand"><span class="brand-dot"></span><span class="brand-name">Cobalt Heron Marketing Solutions</span></div>
    </div>
    <div class="person"><div class="person-name">Linda Hollow</div><div class="person-role">Owner</div></div>
    <ul class="contact-list">
      <li><svg viewBox="0 0 10 10"><path d="M5 0a3.5 3.5 0 0 0-3.5 3.5C1.5 6 5 10 5 10s3.5-4 3.5-6.5A3.5 3.5 0 0 0 5 0zm0 5a1.5 1.5 0 1 1 0-3 1.5 1.5 0 0 1 0 3z"/></svg>2417 Maple Ridge Dr, Longmont CO 80503</li>
      <li><svg viewBox="0 0 10 10"><path d="M2 0l2 2.5-1 1.3a6 6 0 0 0 3.2 3.2l1.3-1L10 8l-1.2 1.6C4.5 10 0 5.5.4 1.2z"/></svg>303.555.0147</li>
      <li><svg viewBox="0 0 10 10"><path d="M0 2h10v6H0zM0 2l5 3.5L10 2"/></svg>lindahollow@cobaltheronmarketing.example</li>
    </ul>
  </section>

  <!-- Business card: web and social -->
  <section class="sheet card card-web">
    <div class="header-band">
      <div class="brand"><span class="brand-dot"></span><span class="brand-name">Cobalt Heron Marketing Solutions</span></div>
    </div>
    <div class="person"><div class="person-name">Linda Hollow</div><div class="person-role">Owner</div></div>
    <ul class="contact-list">
      <li><svg viewBox="0 0 10 10"><circle cx="5" cy="5" r="4.5"/></svg>cobaltheronmarketing.example</li>
      <li><svg viewBox="0 0 10 10"><rect x=".5" y=".5" width="9" height="9" rx="2"/></svg>@LHollow</li>
      <li><svg viewBox="0 0 10 10"><path d="M2 0l2 2.5-1 1.3a6 6 0 0 0 3.2 3.2l1.3-1L10 8l-1.2 1.6C4.5 10 0 5.5.4 1.2z"/></svg>303.555.0147</li>
    </ul>
  </section>

  <!-- Business card: dark reverse -->
  <section class="sheet card card-dark">
    <div class="brand"><span class="brand-dot"></span><span class="brand-name">Cobalt Heron<br>Marketing Solutions</span></div>
    <div class="accent"></div>
  </section>

</body>
</html>
```